Vornel Estates - Chat n’ Cheer Thursday Graphic Invite

We need a graphic design for a corporate reception that we are calling Chat n’ Cheer Thursday. The invite should read:

"QBR invites you to join us at Chat n’ Cheer Thursday

Monday, Jan 22nd
6:30 - 8:30 pm EST

Copper Ladle - Lounge Room

48210 E Pelican Grove Rd
Aventura, FL 33180

Join us for excellent wine and tasty bites at our semi-annual DAW reception. Swing by whenever you can – timing is casual and we'd love to see you there!"

Please feel free to use fun photos from the Copper Ladle gallery: https://www.copperladlegrill.com/photos

Also, please use the QBR logo attached.

Target Market(s)

Corporate professional

Colors
0054AA
0677BA
7BADD7
CADEEF
E8F1F8

Requirements
Must have
• QBR logo, attached verbiage

```html
<!DOCTYPE html>
<html lang="en">
<head>
<meta charset="utf-8">
<title>QBR – Chat n’ Cheer Thursday Invite</title>
<link rel="stylesheet" href="https://fonts.googleapis.com/css2?family=Playfair+Display:wght@400&family=Poppins:wght@400;500;600&display=swap">
<style>
  :root {
    --ink-dark: #0b0b0d;
    --ink-mid: #1a1614;
    --cocktail: #c8371a;
    --cocktail-glow: #f06a2a;
    --bar-amber: #3a2a1c;
    --text-light: #ffffff;
    --brand-deep: #0054AA;
    --brand-mid: #0677BA;
    --brand-soft: #7BADD7;
  }
  * { margin: 0; padding: 0; box-sizing: border-box; }
  html, body {
    width: 1200px;
    height: 1200px;
    overflow: hidden;
    background: var(--ink-dark);
  }
  .invite {
    position: relative;
    width: 1200px;
    height: 1200px;
    overflow: hidden;
    color: var(--text-light);
    font-family: "Poppins", sans-serif;
  }
  .bar-photo {
    position: absolute;
    inset: 0;
    background:
      radial-gradient(ellipse 260px 120px at 420px 500px, var(--cocktail-glow) 0%, var(--cocktail) 45%, transparent 100%),
      radial-gradient(ellipse 220px 380px at 60px 160px, rgba(200,55,26,0.85) 0%, transparent 100%),
      radial-gradient(ellipse 600px 500px at 300px 600px, var(--bar-amber) 0%, transparent 80%),
      linear-gradient(90deg, var(--ink-mid) 0%, var(--ink-dark) 65%, #050506 100%);
  }
  .brand {
    position: absolute;
    left: 800px;
    top: 74px;
    display: flex;
    align-items: center;
    gap: 16px;
  }
  .brand-mark {
    width: 46px;
    height: 46px;
    background: var(--brand-mid);
  }
  .brand-name {
    font-family: "Poppins", sans-serif;
    font-weight: 600;
    font-size: 52px;
    line-height: 1;
    color: var(--brand-soft);
    letter-spacing: 1px;
  }
  .content {
    position: absolute;
    left: 706px;
    top: 230px;
    width: 470px;
  }
  .lead-in {
    font-size: 22px;
    font-weight: 400;
    margin-left: 6px;
  }
  .event-title {
    margin-top: 40px;
    font-family: "Playfair Display", serif;
    font-weight: 400;
    font-size: 82px;
    line-height: 1.13;
    text-transform: uppercase;
    letter-spacing: -0.5px;
  }
  .event-when {
    margin-top: 52px;
    font-size: 31px;
    font-weight: 500;
    line-height: 1.4;
    text-transform: uppercase;
    letter-spacing: 1px;
  }
  .event-when sup { font-size: 17px; vertical-align: 14px; }
  .event-blurb {
    margin-top: 46px;
    font-size: 21px;
    line-height: 1.4;
    font-weight: 400;
    width: 440px;
  }
  .venue {
    margin-top: 54px;
    font-size: 21px;
    line-height: 1.38;
    font-weight: 500;
  }
  .venue-name {
    font-weight: 600;
    text-transform: uppercase;
    letter-spacing: 0.5px;
  }
</style>
</head>
<body>
  <main class="invite">
    <div class="bar-photo" role="img" aria-label="Bartender pouring a red cocktail into a coupe glass on a dark bar counter with blurred bottles behind"></div>

    <div class="brand">
      <span class="brand-mark"></span>
      <span class="brand-name">QBR</span>
    </div>

    <section class="content">
      <p class="lead-in">QBR invites you to join us at</p>
      <h1 class="event-title">Chat n’<br>Cheer<br>Thursday</h1>
      <p class="event-when">Monday, January 22<sup>nd</sup><br>6:30 - 8:30 pm EST</p>
      <p class="event-blurb">Join us for excellent wine and tasty bites at our semi-annual DAW reception. Swing by whenever you can – timing is casual and we'd love to see you there!</p>
      <address class="venue" style="font-style:normal">
        <span class="venue-name">Copper Ladle - Lounge Room</span><br>
        48210 E Pelican Grove Rd<br>
        Aventura, FL 33180
      </address>
    </section>
  </main>
</body>
</html>
```